Harbor Business Cards

I need a business card designed with the following information.

Company Name: Harbor Wealth Management
Name: BriAnne Dockery
Title: Executive Assistant
Cell: (281) 555-0173
Direct Line: (832) 555-0148
Email: brianne@harborwmx.com
Address: 20537 W. Marlowe PKWY Ste. B
Calder Point, ST 77390

I have attached the logo.
I would like it in navy blue and silver.
Thanks.

```html
<!DOCTYPE html>
<html lang="en">
<head>
<meta charset="utf-8">
<title>Harbor Wealth Management – Business Card</title>
<link href="https://fonts.googleapis.com/css2?family=Marcellus&family=Arimo:wght@400;700&display=swap" rel="stylesheet">
<style>
  :root {
    --navy: #0e2240;
    --silver: #b3b3b3;
    --paper: #ffffff;
    --backdrop: #dbe7f5;
  }
  * { box-sizing: border-box; margin: 0; padding: 0; }
  html, body { width: 1200px; height: 1200px; overflow: hidden; }
  body {
    background: var(--backdrop);
    position: relative;
    font-family: "Arimo", Arial, sans-serif;
  }
  .card {
    position: absolute;
    left: 200px;
    width: 800px;
    height: 470px;
    background: var(--paper);
    overflow: hidden;
  }
  .card--front { top: 90px; }
  .card--back { top: 640px; }

  .brand {
    position: absolute;
    display: flex;
    flex-direction: column;
    align-items: center;
    color: var(--navy);
    font-family: "Marcellus", Georgia, serif;
    font-weight: 400;
  }
  .brand__mark {
    background: var(--navy);
    border-radius: 50%;
  }
  .brand__name { line-height: 1; white-space: nowrap; }
  .brand__tag { line-height: 1; white-space: nowrap; }

  .card--front .brand { left: 0; right: 0; top: 118px; }
  .card--front .brand__mark { width: 86px; height: 86px; margin-bottom: 72px; }
  .card--front .brand__name { font-size: 40px; letter-spacing: 0.55em; margin-right: -0.55em; }
  .card--front .brand__tag { font-size: 15px; letter-spacing: 0.3em; margin-top: 16px; margin-right: -0.3em; }

  .card--back .brand { left: 30px; width: 220px; top: 80px; }
  .card--back .brand__mark { width: 52px; height: 52px; margin-bottom: 50px; }
  .card--back .brand__name { font-size: 26px; letter-spacing: 0.5em; margin-right: -0.5em; }
  .card--back .brand__tag { font-size: 10px; letter-spacing: 0.22em; margin-top: 10px; margin-right: -0.22em; }

  .card__sweep { position: absolute; inset: 0; }

  .contact-block {
    position: absolute;
    right: 94px;
    top: 108px;
    color: var(--paper);
    text-align: right;
  }
  .person {
    display: inline-block;
    border-bottom: 2px solid var(--paper);
    padding-bottom: 6px;
  }
  .person__name { font-weight: 700; font-size: 27px; line-height: 1; white-space: nowrap; }
  .person__title { font-weight: 700; font-size: 16px; margin-top: 4px; }

  .contact-list { list-style: none; margin-top: 42px; margin-right: -26px; }
  .contact-list li {
    display: flex;
    justify-content: flex-end;
    align-items: center;
    font-size: 21px;
    line-height: 31.5px;
    gap: 12px;
    white-space: nowrap;
  }
  .contact-list .icon { width: 19px; height: 19px; flex: none; }
  .contact-list .icon--blank { visibility: hidden; }
</style>
</head>
<body>

<section class="card card--front">
  <div class="brand">
    <div class="brand__mark"></div>
    <div class="brand__name">HARBOR</div>
    <div class="brand__tag">WEALTH MANAGEMENT</div>
  </div>
</section>

<section class="card card--back">
  <svg class="card__sweep" viewBox="0 0 800 470" width="800" height="470">
    <path d="M290 0 H800 V470 H22 C190 400 290 260 290 0 Z" fill="var(--silver)"/>
    <path d="M300 0 H800 V470 H34 C200 400 300 260 300 0 Z" fill="var(--navy)"/>
  </svg>

  <div class="brand">
    <div class="brand__mark"></div>
    <div class="brand__name">HARBOR</div>
    <div class="brand__tag">WEALTH MANAGEMENT</div>
  </div>

  <div class="contact-block">
    <div class="person">
      <div class="person__name">BRIANNE DOCKERY</div>
      <div class="person__title">-Executive Assistant</div>
    </div>
    <ul class="contact-list">
      <li>(281) 555-0173
        <svg class="icon" viewBox="0 0 20 20"><circle cx="10" cy="10" r="10" fill="#fff"/><rect x="7" y="4.5" width="6" height="11" rx="1.2" fill="var(--navy)"/><rect x="8" y="6" width="4" height="6.5" fill="#fff"/></svg>
      </li>
      <li>(832) 555-0148
        <svg class="icon" viewBox="0 0 20 20"><circle cx="10" cy="10" r="10" fill="#fff"/><path d="M4.5 8.5 C6 5.5 14 5.5 15.5 8.5 L13.5 9.5 L12.5 8 H7.5 L6.5 9.5 Z" fill="var(--navy)"/><rect x="6" y="10" width="8" height="4.5" rx="1" fill="var(--navy)"/></svg>
      </li>
      <li>brianne@harborwmx.com
        <svg class="icon" viewBox="0 0 20 20"><circle cx="10" cy="10" r="10" fill="#fff"/><rect x="5" y="6.5" width="10" height="7" rx="1" fill="var(--navy)"/><path d="M5.5 7.2 L10 10.8 L14.5 7.2" stroke="#fff" stroke-width="1.1" fill="none"/></svg>
      </li>
      <li>20537 W. Marlowe PKWY Ste. B
        <svg class="icon" viewBox="0 0 20 20"><circle cx="10" cy="10" r="10" fill="#fff"/><path d="M10 16 C7 12 6 10.5 6 8.5 A4 4 0 0 1 14 8.5 C14 10.5 13 12 10 16 Z" fill="var(--navy)"/><circle cx="10" cy="8.5" r="1.6" fill="#fff"/></svg>
      </li>
      <li>Calder Point, ST 77390
        <svg class="icon icon--blank" viewBox="0 0 20 20"></svg>
      </li>
    </ul>
  </div>
</section>

</body>
</html>
```